Audio Visual & Broadcast Installing Company needs a Web Site Design

We need a website design for our company Corvane Ltd. We are a small company that does Audio Visual and broadcast installations. We are looking to expand our business and need a professional web presence. All work completed by us is done to a very high standard and it’s this attention to detail that sets us apart from our competitors. Our projects include doing fibre optics at major sporting events; installing and commissioning bespoke control systems on super yachts and installing the latest systems in luxury homes.

We provide the following services:
System design
On-site installation
Rack building
Pre-fabricated cable looms
Fibre optic cabling

We would like a website that gives details of our services and provides contact information. Our customers are other businesses and our website needs to reflect this. The flyer attached will be used to promote the company and we would like the website to follow this theme. Please use the colours from our logo, as the colour scheme. We know that our colours are bright and we don’t want them to overwhelm the site. With our website we want to communicate that we are professional and provide a quality service.
NB UPDATE: please use stock images for any graphical elements.

The following 3 sites belong to some of our competitors. The first 2, we DON'T like because they don't project a professional feeling. The last one, 'vellumspire', is better as it provides the required information in a clear, simple form.

http://www.plomquist-example.com/

http://www.heronfieldlinkworks-example.com/

http://www.vellumspire-example.com/

We really like the following site, it feels professional and high end without too many flashy graphics. We want something that is fast to load but still shows the high end quality of our work.

http://osmerdalegroup-example.com/

Pages/Sections

Home
On site installation
Rack building and cable looms
Fibre optics
Portfolio (this will be limited to start with but must be easy to expand and add new projects)
Updates

Target Market(s)

Businesses operating in the following areas:
Audio Vision, Broadcasting, Home Automation, Events

Industry/Entity Type

Broadcasting

Coding

Coded - Design and coding required

Number of Pages Required

4 page

Font styles to use
Other font styles liked:
• similar to attached flyer

Requirements
Must have
• The same theme as the 'flyer1' attachment.

```html
<!DOCTYPE html>
<html lang="en">
<head>
<meta charset="utf-8">
<title>Corvane Ltd — Audio Visual &amp; Broadcast Installation</title>
<link rel="stylesheet" href="https://fonts.googleapis.com/css2?family=Roboto:wght@300;400;500;700;900&display=swap">
<style>
:root{
  --blue:#1f74e0;
  --blue-deep:#1662c4;
  --red:#e0202f;
  --ink:#222;
  --muted:#6b6b6b;
  --dark:#262626;
  --darker:#1c1c1c;
  --footer:#232323;
  --line:#e3e3e3;
  --white:#fff;
}
*{box-sizing:border-box;margin:0;padding:0}
html,body{width:1200px;height:2696px;overflow:hidden}
body{font-family:"Roboto",Arial,sans-serif;color:var(--ink);background:var(--white);position:relative}
a{color:inherit;text-decoration:none}

/* header */
.site-header{height:56px;display:flex;align-items:center;padding:0 140px;background:var(--white);position:relative;z-index:2}
.brand{display:flex;align-items:center;gap:8px;font-weight:700;font-size:20px;color:var(--ink)}
.brand-mark{width:14px;height:14px;background:var(--red)}
.main-nav{display:flex;gap:22px;margin-left:70px;font-size:9.5px;font-weight:500;text-transform:uppercase;letter-spacing:.4px}
.main-nav a{color:#333}
.main-nav a.active{color:var(--blue);border-bottom:2px solid var(--blue);padding-bottom:4px}
.header-contact{margin-left:auto;display:flex;align-items:center;gap:16px}
.phone-block{text-align:right;line-height:1.1}
.phone-block small{display:block;font-size:8px;color:var(--muted)}
.phone-block strong{font-size:17px;color:var(--red);font-weight:700}
.btn{display:inline-block;font-weight:700;text-transform:uppercase;color:var(--white);border-radius:2px}
.btn-quote{background:var(--blue);font-size:10px;padding:9px 14px}

/* hero */
.hero{height:604px;position:relative;overflow:hidden}
.hero-photo{position:absolute;inset:0;background:radial-gradient(ellipse at 60% 70%,#7a4a2a 0%,#3a2a22 35%,#141416 75%)}
.hero-content{position:absolute;top:370px;left:0;right:0;text-align:center;color:var(--white)}
.hero-title{font-size:48px;font-weight:900;letter-spacing:.5px}
.hero-sub{font-size:20px;font-weight:500;margin-top:4px}
.btn-read{background:var(--red);font-size:15px;padding:15px 38px;margin-top:26px}
.hero-dots{position:absolute;top:574px;left:0;right:0;display:flex;justify-content:center;gap:12px}
.hero-dots span{width:10px;height:10px;border-radius:50%;background:rgba(255,255,255,.55)}
.hero-dots span.on{background:var(--white)}

/* services */
.services{height:420px;padding-top:48px;text-align:center}
.section-title{font-size:20px;font-weight:700;letter-spacing:.5px}
.section-title::after{content:"";display:block;width:40px;height:2px;background:var(--blue);margin:10px auto 0}
.service-list{display:flex;justify-content:center;gap:38px;margin-top:64px}
.service{width:148px}
.service svg{width:60px;height:60px}
.service h3{font-size:17px;font-weight:500;margin-top:16px}
.service p{font-size:11px;line-height:1.5;color:var(--muted);margin-top:10px}

/* welcome */
.welcome{height:520px;display:flex}
.welcome-photo{width:600px;background:linear-gradient(135deg,#8fa3b8 0%,#c9d3dc 45%,#6f7e8c 100%)}
.welcome-panel{width:600px;background:var(--dark);color:var(--white);padding:52px 80px 0 52px}
.welcome-panel .kicker{font-size:18px;font-weight:500}
.welcome-panel h2{font-size:34px;font-weight:700;letter-spacing:.5px;margin-top:4px}
.welcome-panel h2::after{content:"";display:block;width:40px;height:2px;background:var(--red);margin-top:10px}
.welcome-panel p{font-size:12px;line-height:1.7;color:#cfcfcf;margin-top:22px}
.welcome-panel .cta{font-size:13px;font-weight:500;text-transform:uppercase;margin-top:40px}
.contact-line{display:flex;align-items:center;gap:26px;margin-top:24px;border-top:1px solid #3a3a3a;padding-top:18px}
.contact-line svg{width:20px;height:20px;fill:var(--white)}
.contact-line small{display:block;font-size:11px;color:#aaa}
.contact-line span{font-size:14px}

/* innovation */
.innovation{height:592px;display:flex}
.innovation-panel{width:600px;background:var(--blue);color:var(--white);padding:72px 110px 0 80px}
.innovation-panel h2{font-size:24px;font-weight:700;text-transform:uppercase;line-height:1.3}
.innovation-panel p{font-size:12px;line-height:1.7;margin-top:22px;color:#e5eefc}
.btn-outline{border:2px solid var(--white);font-size:12px;padding:11px 18px;margin-top:56px;text-transform:none}
.innovation-photo{width:600px;background:radial-gradient(ellipse at 40% 60%,#d7e6f2 0%,#7a9cb8 40%,#2d4a66 100%)}

/* newsletter */
.newsletter{height:216px;text-align:center;padding-top:44px}
.newsletter-form{display:flex;justify-content:center;gap:30px;margin-top:46px}
.newsletter-form span{width:230px;height:42px;border:1px solid var(--line);text-align:left;font-size:12px;color:#999;padding:13px 14px}
.btn-subscribe{background:var(--red);font-size:13px;padding:14px 30px}

/* footer */
.site-footer{height:248px;background:var(--footer);color:#cfcfcf;display:flex;padding:40px 0 0 200px}
.footer-brand{width:260px;display:flex;align-items:center;gap:10px;font-size:34px;font-weight:700;color:var(--white);align-self:flex-start;margin-top:38px}
.footer-brand .brand-mark{width:22px;height:22px}
.footer-col{width:340px;font-size:11px;line-height:1.9}
.footer-col.menu{width:140px}
.footer-col h4{font-size:12px;font-weight:700;color:var(--white);text-transform:uppercase;margin-bottom:10px}
.footer-col .row{display:flex;align-items:center;gap:12px;margin-bottom:10px}
.footer-col .row svg{width:12px;height:12px;fill:#cfcfcf}
.social{display:flex;gap:8px}
.social span{width:24px;height:24px;border-radius:50%;background:var(--blue)}
.copyright{height:40px;background:var(--darker);color:#888;font-size:10px;text-align:center;line-height:40px}
</style>
</head>
<body>

<header class="site-header">
  <div class="brand"><span class="brand-mark"></span>Corvane</div>
  <nav class="main-nav">
    <a class="active" href="#">Home</a>
    <a href="#">On site installation</a>
    <a href="#">Rack building and cable looms</a>
    <a href="#">Fibre optics</a>
    <a href="#">Portfolio</a>
    <a href="#">Contact us</a>
  </nav>
  <div class="header-contact">
    <div class="phone-block"><small>Call us now</small><strong>01632 960-418</strong></div>
    <a class="btn btn-quote" href="#">Get a quote</a>
  </div>
</header>

<section class="hero">
  <div class="hero-photo" role="img" aria-label="Close view of a lit broadcast audio mixing console in a dark studio"></div>
  <div class="hero-content">
    <h1 class="hero-title">AV SYSTEM INSTALLATION</h1>
    <p class="hero-sub">Broadcast and Audio Visual Industries</p>
    <a class="btn btn-read" href="#">Read more</a>
  </div>
  <div class="hero-dots"><span></span><span></span><span class="on"></span><span></span><span></span></div>
</section>

<section class="services">
  <h2 class="section-title">OUR SERVICES</h2>
  <div class="service-list">
    <div class="service">
      <svg viewBox="0 0 60 60" fill="none" stroke="var(--blue)" stroke-width="3"><path d="M30 22 L20 56 M30 22 L40 56 M23 44 H37"/><circle cx="30" cy="18" r="4" fill="var(--blue)"/><path d="M20 8 A14 14 0 0 0 20 28 M40 8 A14 14 0 0 1 40 28"/></svg>
      <h3>System Design</h3>
      <p>Clear planning of every signal path, shaped around how your team works each day.</p>
    </div>
    <div class="service">
      <svg viewBox="0 0 60 60" fill="var(--blue)"><path d="M26 4h8l2 8 6 3 7-4 6 6-4 7 3 6 8 2v8l-8 2-3 6 4 7-6 6-7-4-6 3-2 8h-8l-2-8-6-3-7 4-6-6 4-7-3-6-8-2v-8l8-2 3-6-4-7 6-6 7 4 6-3z"/><circle cx="30" cy="30" r="9" fill="#fff"/></svg>
      <h3>On-site installation</h3>
      <p>Our engineers fit and commission systems on site, tidy and tested before handover.</p>
    </div>
    <div class="service">
      <svg viewBox="0 0 60 60" fill="var(--blue)"><rect x="8" y="6" width="44" height="14" rx="2"/><rect x="8" y="23" width="44" height="14" rx="2"/><rect x="8" y="40" width="44" height="14" rx="2"/><g fill="#fff"><rect x="14" y="12" width="20" height="2"/><rect x="14" y="29" width="20" height="2"/><rect x="14" y="46" width="20" height="2"/></g></svg>
      <h3>Rack building</h3>
      <p>Racks built and wired in our workshop, labelled and ready to drop into place.</p>
    </div>
    <div class="service">
      <svg viewBox="0 0 60 60" fill="none" stroke="var(--blue)" stroke-width="3"><rect x="20" y="16" width="20" height="22" rx="3" fill="var(--blue)"/><path d="M25 6v10M35 6v10M30 38v8c0 6-8 6-8 12"/></svg>
      <h3>Pre-fabricated cable looms</h3>
      <p>Looms made to length and tested, cutting time on site and keeping runs neat.</p>
    </div>
    <div class="service">
      <svg viewBox="0 0 60 60" fill="none" stroke="var(--blue)" stroke-width="3"><path d="M8 50c10-4 14-14 22-20s16-8 22-18"/><path d="M8 42c10-4 14-12 20-18s14-6 20-14"/><circle cx="52" cy="12" r="3" fill="var(--blue)"/><circle cx="48" cy="10" r="3" fill="var(--blue)"/></svg>
      <h3>Fibre optic cabling</h3>
      <p>Fibre runs for venues and events, terminated and certified to a high standard.</p>
    </div>
  </div>
</section>

<section class="welcome">
  <div class="welcome-photo" role="img" aria-label="Engineer at a desk reviewing system charts on a laptop and tablet"></div>
  <div class="welcome-panel">
    <p class="kicker">WELCOME TO</p>
    <h2>CORVANE</h2>
    <p>Corvane Ltd provides cabling services for the broadcast and audio visual industries. We specialise in fibre and rack installation, which has come to represent our high end work. Our team puts precision first and every installation is finished to the same careful standard.</p>
    <p class="cta">For a quote or to discuss your project</p>
    <div class="contact-line">
      <svg viewBox="0 0 24 24"><path d="M2 5h20v14H2z M2 5l10 8 10-8" fill="none" stroke="#fff" stroke-width="2"/></svg>
      <div><small>E-mail</small><span>hello@corvane-example.com</span></div>
    </div>
    <div class="contact-line">
      <svg viewBox="0 0 24 24"><path d="M6 2l4 5-2 3c1 3 3 5 6 6l3-2 5 4-2 4C10 22 2 14 2 4z"/></svg>
      <div><small>Call us on</small><span>07700 900-352</span></div>
    </div>
  </div>
</section>

<section class="innovation">
  <div class="innovation-panel">
    <h2>Making the connections that digital innovation demands</h2>
    <p>From stadium fibre runs to yacht control rooms, we design, build and commission systems that stay reliable under pressure. Every project is planned in detail and delivered on schedule by our own engineers, with clear records left behind for your team.</p>
    <a class="btn btn-outline" href="#">Read More</a>
  </div>
  <div class="innovation-photo" role="img" aria-label="Hand reaching toward a glowing digital network interface"></div>
</section>

<section class="newsletter">
  <h2 class="section-title">NEWSLETTER SIGNUP</h2>
  <div class="newsletter-form">
    <span>Name</span>
    <span>E-mail</span>
    <a class="btn btn-subscribe" href="#">Subscribe</a>
  </div>
</section>

<footer class="site-footer">
  <div class="footer-brand"><span class="brand-mark"></span>Corvane</div>
  <div class="footer-col">
    <h4>Contact us</h4>
    <div class="row"><svg viewBox="0 0 24 24"><path d="M12 2a7 7 0 0 0-7 7c0 5 7 13 7 13s7-8 7-13a7 7 0 0 0-7-7z"/></svg>42 Ashdown Mews, Harlow, CM20 3QT</div>
    <div class="row"><svg viewBox="0 0 24 24"><path d="M6 2l4 5-2 3c1 3 3 5 6 6l3-2 5 4-2 4C10 22 2 14 2 4z"/></svg>01632 960-418</div>
    <div class="row"><svg viewBox="0 0 24 24"><path d="M2 5h20v14H2z"/></svg>office@corvane-example.com</div>
  </div>
  <div class="footer-col menu">
    <h4>Menu</h4>
    Home<br>On site installation<br>Rack building and cable looms<br>Fibre optics<br>Portfolio<br>Contact us
  </div>
  <div class="footer-col">
    <h4>Follow us</h4>
    <div class="social"><span></span><span></span><span></span></div>
  </div>
</footer>
<div class="copyright">Copyright © 2017 All Rights Reserved</div>

</body>
</html>
```